Accounting practice seeks business card redesign with existing logo

Accounting practice has logo and slogan but more needs modern professional business revision. Must be in a file format ready to print quality business cards.

Open to artistic ideas but for the brand recognition the features below must be incorporated:

- Logo: attached in EPS format (Logo now blue)
- Slogan: Proven Business Solutions... That Work! (in orange legible handwriting type font)
- Name: Daniel T Hoxley RBA AAT JP (letters in smaller font)
- Phone icon: 1800 531 908
- Mobile phone icon: 0412 385 714
- Web icon: www.kelnovagroup.com.au
- Email icon: admin@kelnovagroup.com.au
- See pics for dark blue/med blue line at bottom, this is a necessity.
- Globe that forms the 'dot' in the 'I' of KelNova is attached. It is too big at present.
- Rear side: pic attached. Note my logo is a watermark. I Will provide slightly revised wording details later. Please allow for a small white space at bottom of rear of card to write notes/appointment details.

I am open to ideas but must retain the above for brand recognition.

```html
<!DOCTYPE html>
<html lang="en">
<head>
<meta charset="utf-8">
<title>KelNova – Business Card</title>
<link href="https://fonts.googleapis.com/css2?family=Cinzel:wght@600&family=Didact+Gothic&display=swap" rel="stylesheet">
<style>
  :root {
    --stage: #1c1c1e;
    --paper: #ffffff;
    --navy: #1b2456;
    --navy-deep: #141b45;
    --navy-soft: #2c3a7e;
    --mid-blue: #3d8cc4;
    --mid-blue-light: #58a6d6;
    --ink: #1d2a5c;
    --ink-soft: #3b3f4a;
    --orange: #e0701e;
    --pale-text: #d9def2;
    --note-strip: #f1f1f3;
  }
  * { box-sizing: border-box; margin: 0; padding: 0; }
  html, body { width: 1200px; height: 871px; overflow: hidden; background: var(--stage); }
  .canvas {
    width: 1200px; height: 871px;
    display: flex; flex-direction: column; align-items: center; justify-content: center; gap: 30px;
  }
  .card {
    position: relative; width: 680px; height: 389px; overflow: hidden;
    box-shadow: 0 14px 30px rgba(0,0,0,.55);
  }

  /* ---------- Front ---------- */
  .card--front { background: var(--paper); }
  .brand { position: absolute; left: 52px; top: 112px; }
  .brand__name {
    display: flex; align-items: center; gap: 10px;
    font-family: "Didact Gothic", sans-serif; font-size: 52px; letter-spacing: 2px;
    color: var(--mid-blue); line-height: 1;
  }
  .brand__dot { width: 14px; height: 14px; border-radius: 50%; background: var(--mid-blue); }
  .brand__slogan {
    margin-top: 14px;
    font-family: "Cinzel", serif; font-size: 15px; letter-spacing: 1px; color: var(--orange);
  }
  .holder { position: absolute; left: 374px; top: 118px; }
  .holder__name {
    font-family: "Cinzel", serif; font-size: 16px; letter-spacing: 1.2px; color: var(--ink);
  }
  .contacts { list-style: none; margin-top: 24px; }
  .contacts li {
    display: flex; align-items: center; gap: 14px; height: 25px;
    font-family: "Didact Gothic", sans-serif; font-size: 15px; color: var(--ink-soft); letter-spacing: .6px;
  }
  .contacts svg { width: 16px; height: 16px; flex: none; }
  .base-band { position: absolute; left: 0; bottom: 0; width: 680px; height: 62px; }

  /* ---------- Back ---------- */
  .card--back { background: linear-gradient(135deg, var(--navy-soft) 0%, var(--navy) 55%, var(--navy-deep) 100%); }
  .watermark {
    position: absolute; font-family: "Didact Gothic", sans-serif; color: rgba(255,255,255,.07);
    letter-spacing: 6px; line-height: 1; white-space: nowrap;
  }
  .watermark--left { left: -20px; top: 120px; font-size: 110px; }
  .watermark--right { right: -30px; top: 40px; font-size: 110px; }
  .mission {
    position: absolute; left: 0; right: 0; top: 38px; text-align: center;
    font-family: "Didact Gothic", sans-serif; font-size: 14px; letter-spacing: 3px; line-height: 1.6;
    color: var(--pale-text); text-transform: uppercase;
  }
  .services {
    position: absolute; top: 150px; list-style: none;
    font-family: "Didact Gothic", sans-serif; font-size: 13px; letter-spacing: 2.5px;
    color: var(--pale-text); text-transform: uppercase;
  }
  .services--left { left: 80px; top: 176px; }
  .services--right { left: 380px; top: 150px; }
  .services li { display: flex; align-items: center; gap: 18px; height: 24px; }
  .services li::before {
    content: ""; width: 11px; height: 11px; border-radius: 50%;
    background: var(--pale-text); opacity: .85;
  }
  .note-strip { position: absolute; left: 0; right: 0; bottom: 0; height: 78px; background: var(--note-strip); }
</style>
</head>
<body>
<main class="canvas">

  <section class="card card--back" aria-label="Card reverse">
    <span class="watermark watermark--left" aria-hidden="true">KelNova</span>
    <span class="watermark watermark--right" aria-hidden="true">KelNova</span>
    <p class="mission">Your trusted provider of quality business<br>and accounting solutions, proven to work for<br>small to medium business and tradies</p>
    <ul class="services services--left">
      <li>Bookkeeping</li>
      <li>BAS</li>
      <li>Cloud Accounting</li>
      <li>Debt Recovery</li>
    </ul>
    <ul class="services services--right">
      <li>Business Advice</li>
      <li>ATO Assistance</li>
      <li>Office Technology</li>
      <li>And much more....</li>
    </ul>
    <div class="note-strip"></div>
  </section>

  <section class="card card--front" aria-label="Card front">
    <div class="brand">
      <div class="brand__name">KelNova<span class="brand__dot"></span></div>
      <p class="brand__slogan">Proven Business Solutions</p>
    </div>

    <div class="holder">
      <h1 class="holder__name">Daniel T Hoxley RBA AAT JP</h1>
      <ul class="contacts">
        <li>
          <svg viewBox="0 0 16 16" aria-hidden="true"><path fill="#1d2a5c" d="M2 6c0-2 3-3 6-3s6 1 6 3v1h-3V5.5H5V7H2zM4 8h8l1.5 5h-11z"/><circle cx="8" cy="10.5" r="1.4" fill="#fff"/></svg>
          1800 531 908
        </li>
        <li>
          <svg viewBox="0 0 16 16" aria-hidden="true"><rect x="4.5" y="1.5" width="7" height="13" rx="1.3" fill="none" stroke="#1d2a5c" stroke-width="1.4"/><line x1="7" y1="12.3" x2="9" y2="12.3" stroke="#1d2a5c" stroke-width="1.2"/></svg>
          0412 385 714
        </li>
        <li>
          <svg viewBox="0 0 16 16" aria-hidden="true"><rect x="1.5" y="3.5" width="13" height="9" fill="none" stroke="#1d2a5c" stroke-width="1.4"/><path d="M1.5 3.5 8 9l6.5-5.5" fill="none" stroke="#1d2a5c" stroke-width="1.4"/></svg>
          admin@kelnovagroup.com.au
        </li>
        <li>
          <svg viewBox="0 0 16 16" aria-hidden="true"><circle cx="8" cy="8" r="6.3" fill="none" stroke="#1d2a5c" stroke-width="1.4"/><ellipse cx="8" cy="8" rx="2.6" ry="6.3" fill="none" stroke="#1d2a5c" stroke-width="1.1"/><line x1="1.7" y1="8" x2="14.3" y2="8" stroke="#1d2a5c" stroke-width="1.1"/></svg>
          www.kelnovagroup.com.au
        </li>
      </ul>
    </div>

    <svg class="base-band" viewBox="0 0 680 62" aria-hidden="true">
      <defs>
        <linearGradient id="midBlue" x1="0" x2="1" y1="0" y2="0">
          <stop offset="0" stop-color="var(--mid-blue-light)"/>
          <stop offset="1" stop-color="var(--mid-blue)"/>
        </linearGradient>
      </defs>
      <polygon points="0,0 312,0 270,62 0,62" fill="url(#midBlue)"/>
      <polygon points="324,16 680,16 680,62 282,62" fill="var(--navy)"/>
    </svg>
  </section>

</main>
</body>
</html>
```